Boutique Wealth management firm needs a new business card design

I want to update my business card design to be more consistent with the look and feel of my website (www.brisvane-wealth.com). I would like to incorporate an ivory parchment background and am open to switching from the current "portrait" layout to a more traditional "landscape" orientation. The final design should convey stability and exclusivity and I want something in PDF format that is ready to send to the printer

Thank you all for taking the time to submit your designs for my project. I've made my decision and picked the design I like best. Thanks again!

```html
<!DOCTYPE html>
<html lang="en">
<head>
<meta charset="utf-8">
<title>Brisvane Wealth Advisory – Business Card</title>
<link rel="stylesheet" href="https://fonts.googleapis.com/css2?family=Carlito:wght@400;700&display=swap">
<style>
  :root {
    --wine: #6e1230;
    --wine-dark: #561026;
    --ivory: #fdfbdc;
    --parchment-light: #f6ead0;
    --parchment-dark: #e2c48f;
    --ink: #2a2420;
    --backdrop: #e9e6e1;
    --vineyard-dark: #3d3a1c;
    --vineyard-mid: #5a5e26;
    --sunset: #e8a35a;
  }
  * { box-sizing: border-box; margin: 0; padding: 0; }
  html, body {
    width: 1200px; height: 900px; overflow: hidden;
    background: var(--backdrop);
    font-family: "Carlito", "Calibri", sans-serif;
  }
  .stage {
    width: 1200px; height: 900px;
    display: flex; align-items: center; justify-content: center;
  }
  .card {
    position: relative;
    width: 1050px; height: 600px;
    background: var(--ivory);
    box-shadow: 0 10px 30px rgba(0,0,0,.18);
    overflow: hidden;
  }
  .band {
    position: absolute; left: 0; right: 0; height: 38px;
    background: var(--wine);
  }
  .band--top { top: 0; }
  .band--bottom { bottom: 0; }
  .brand {
    position: absolute; left: 0; top: 38px;
    width: 300px; height: 290px;
    background: linear-gradient(135deg, var(--parchment-light) 0%, var(--parchment-dark) 100%);
    display: flex; flex-direction: column; justify-content: center;
    padding-left: 34px;
  }
  .brand__name {
    color: var(--wine);
    font-weight: 700;
    font-size: 54px;
    letter-spacing: 1px;
    line-height: 1;
    text-transform: uppercase;
  }
  .brand__tag {
    color: var(--wine);
    font-weight: 700;
    font-size: 26px;
    margin-top: 6px;
    padding-left: 60px;
  }
  .vineyard {
    position: absolute; left: 300px; top: 38px;
    width: 460px; height: 200px;
  }
  .person {
    position: absolute; left: 360px; top: 268px;
  }
  .person__name {
    color: var(--wine);
    font-size: 40px; font-weight: 700;
    letter-spacing: .5px;
  }
  .person__role {
    color: var(--ink);
    font-size: 24px;
    margin-left: 120px;
  }
  .license {
    position: absolute; right: 60px; top: 330px;
    color: var(--ink); font-size: 26px; font-weight: 700;
  }
  .contact {
    position: absolute; left: 110px; top: 380px;
    list-style: none;
    color: var(--ink); font-size: 25px;
  }
  .contact__item {
    display: flex; align-items: center; gap: 14px;
    height: 34px;
  }
  .contact__item--address { margin-top: 34px; }
  .contact__icon { width: 20px; height: 20px; fill: var(--wine); flex: none; }
</style>
</head>
<body>
<main class="stage">
  <article class="card">
    <div class="band band--top"></div>

    <div class="brand">
      <span class="brand__name">Brisvane</span>
      <span class="brand__tag">Wealth Advisory</span>
    </div>

    <svg class="vineyard" viewBox="0 0 460 200" role="img" aria-label="Photograph of vineyard rows on rolling hills at sunset">
      <defs>
        <linearGradient id="vineyardTone" x1="0" y1="0" x2="1" y2="1">
          <stop offset="0" stop-color="var(--sunset)"/>
          <stop offset=".35" stop-color="var(--vineyard-dark)"/>
          <stop offset="1" stop-color="var(--vineyard-mid)"/>
        </linearGradient>
      </defs>
      <polygon points="0,0 460,0 400,200 0,200" fill="url(#vineyardTone)"/>
    </svg>

    <div class="person">
      <h1 class="person__name">DANA HOLLOWAY, CFP</h1>
      <p class="person__role">Principal</p>
    </div>

    <p class="license">CA License #0K71806</p>

    <ul class="contact">
      <li class="contact__item">
        <svg class="contact__icon" viewBox="0 0 20 20"><path d="M4 1h4l1.5 4.5-2.5 1.5a11 11 0 0 0 6 6l1.5-2.5L19 12v4c0 1.5-1 2-2 2C8 18 2 12 2 3c0-1 .5-2 2-2z"/></svg>
        <span>925-555-0148</span>
      </li>
      <li class="contact__item">
        <svg class="contact__icon" viewBox="0 0 20 20"><rect x="1" y="4" width="18" height="12" rx="1"/><path d="M2 5l8 6 8-6" fill="none" stroke="var(--ivory)" stroke-width="1.5"/></svg>
        <span>dana@brisvane-wealth.com</span>
      </li>
      <li class="contact__item">
        <svg class="contact__icon" viewBox="0 0 20 20"><path d="M10 1a9 9 0 1 0 5 16.5l-1-1.6A7 7 0 1 1 17 10v1a1.5 1.5 0 0 1-3 0V6h-2v1a4 4 0 1 0 .5 5.5A3.5 3.5 0 0 0 19 11v-1a9 9 0 0 0-9-9zm0 11a2 2 0 1 1 0-4 2 2 0 0 1 0 4z"/></svg>
        <span>www.brisvane-wealth.com</span>
      </li>
      <li class="contact__item contact__item--address">
        <svg class="contact__icon" viewBox="0 0 20 20"><path d="M10 1a6 6 0 0 0-6 6c0 4.5 6 12 6 12s6-7.5 6-12a6 6 0 0 0-6-6zm0 8.5a2.5 2.5 0 1 1 0-5 2.5 2.5 0 0 1 0 5z"/></svg>
        <span>2870 Orchard Ln. #214, Livermore, CA 94550</span>
      </li>
    </ul>

    <div class="band band--bottom"></div>
  </article>
</main>
</body>
</html>
```